Fresh & Clean *NEW* BUSINESS CARD Needed - OPTOMETRY Clinic/Optical

High-tech optometry practice with 3 doctors seeking new business card.  We provide eye exams, sell, designer glasses/contacts/specialty eyewear and treat ocular diseases.  For our business cards, we are seeking fresh, clean, and crisp design as we grow our team (staffing change).  Simply adding doctors is making the card look busy/cluttered.
 Looking for professional, less cluttered look yet still have our logo, doctor names, phone, address, and website....If possible!  :)
Names:
Marisol Pettigrew, O.D.
Ray Bellamy, O.D.
Nora Vantreese, O.D.
Phone: 555-214-6038
Website: www.BrightLensStudio.example
Address:  418 Harlan P. Moody, Fairhaven Springs, NV 70000
Ultimately we have the main business card with all doctor sames and that card has two versions  (front is always the same).  The back has two designs (1) displays next appointment time/date, (2) for "general use" (non-appointment.)    I have attached what we have used in the past.  
We also need a design template for each team member in our practice with their name, title, and email.   Those should be designed with the "general use" back (see attached).
**Open to entirely new design so don't feel obligated to keep current format.  Need new perspective!  Also including our watermark and some other design features we have consistently used in past in our portfolio.  Included are two options for logos--vertical and horizontal.
**I also would like to remove "Member of Optic Guild" on our logo if possible**
 Other image files available upon request.

Target Market(s)

New patient & Current Patients

Industry/Entity Type

Optometry

Contact Information for Business Card

High-tech optometry practice with 3 doctors seeking new business card.  We provide eye exams, sell, designer glasses/contacts/specialty eyewear and treat ocular diseases.  For our business cards, we are seeking fresh, clean, and crisp design as we grow our team (staffing change).  Simply adding doctors is making the card look busy/cluttered.  Looking for professional, less cluttered look yet still have our logo, doctor names, phone, address, and website....If possible!  :) Names: Marisol Pettigrew, O.D. Ray Bellamy, O.D. Nora Vantreese, O.D. Phone: 555-214-6038 Website: www.BrightLensStudio.example Address:  418 Harlan P. Moody, Fairhaven Springs, NV 70000 Ultimately we have the main business card with all doctor sames and that card has two versions  (front is always the same).  The back has two designs (1) displays next appointment time/date, (2) for "general use" (non-appointment.)    I have attached what we have used in the past.   We also need a design template for each team member in our practice with their name, title, and email.   Those should be designed with the "general use" back (see attached). **Open to entirely new design so don't feel obligated to keep current format.  Need new perspective!  Also including our watermark and some other design features we have consistently used in past in our portfolio.  Included are two options for logos--vertical and horizontal. **I also would like to remove "Member of Optic Guild" on our logo if possible**  Other image files available upon request.

Font styles to use
Other font styles liked:
• We have used Montserrat / Yellowtail in the past

Colors

Designer to choose colors to be used in the design.

Requirements
Must have
• Clean & Fresh Design with Logo / Info provided in description. Horizontal orientation. **I have included the CMYK colors we currently have in our logo.
Should not have
• Cluttered

```html
<!DOCTYPE html>
<html lang="en">
<head>
<meta charset="utf-8">
<title>Bright Lens Studio – Business Card</title>
<link rel="stylesheet" href="https://fonts.googleapis.com/css2?family=Montserrat:ital,wght@0,400;1,400&family=Quicksand:wght@400&display=swap">
<style>
  :root {
    --stage: #a7a7a7;
    --card: #ffffff;
    --ink: #6d6e71;
    --sky: #a6dce7;
    --gold: #d8aa1c;
  }
  * { margin: 0; padding: 0; box-sizing: border-box; }
  html, body {
    width: 1200px; height: 1200px; overflow: hidden;
    background: var(--stage);
  }
  .card {
    position: absolute;
    left: 151px; width: 900px; height: 512px;
    background: var(--card);
  }
  .card--front { top: 72px; }
  .card--back { top: 612px; }

  .brand {
    position: absolute;
    display: flex; align-items: center; gap: 26px;
  }
  .brand__dot {
    border-radius: 50%;
    background: var(--sky);
    flex: none;
  }
  .brand__name {
    font-family: "Quicksand", sans-serif;
    font-weight: 400;
    color: var(--ink);
    white-space: nowrap;
    letter-spacing: 1px;
  }
  .card--front .brand { left: 96px; top: 50px; }
  .card--front .brand__dot { width: 104px; height: 104px; }
  .card--front .brand__name { font-size: 60px; }

  .swoosh { position: absolute; left: 0; top: 0; }

  .doctors {
    position: absolute; left: 496px; top: 200px;
    list-style: none;
    font-family: "Montserrat", sans-serif;
    font-style: italic;
    font-size: 25px;
    line-height: 36px;
    color: var(--ink);
  }

  .contact {
    position: absolute; left: 64px; top: 344px;
    list-style: none;
    font-family: "Montserrat", sans-serif;
    font-size: 22px;
    line-height: 36.5px;
    color: var(--ink);
  }
  .contact__item { display: flex; align-items: center; gap: 14px; }
  .contact__icon { width: 20px; height: 20px; flex: none; }

  .card--back .brand {
    left: 0; right: 0; top: 0; bottom: 0;
    justify-content: center;
  }
  .card--back .brand__dot { width: 150px; height: 150px; }
  .card--back .brand__name { font-size: 58px; }
</style>
</head>
<body>

<section class="card card--front">
  <svg class="swoosh" width="900" height="512" viewBox="0 0 900 512" aria-hidden="true">
    <polygon points="30,305 496,148 871,148 871,176 499,176" fill="var(--sky)"/>
  </svg>

  <div class="brand">
    <span class="brand__dot"></span>
    <span class="brand__name">Bright Lens Studio</span>
  </div>

  <ul class="doctors">
    <li>Marisol Pettigrew, O.D.</li>
    <li>Ray Bellamy, O.D.</li>
    <li>Nora Vantreese, O.D.</li>
  </ul>

  <ul class="contact">
    <li class="contact__item">
      <svg class="contact__icon" viewBox="0 0 20 20" aria-hidden="true">
        <path d="M5 2.5 L8 6 L6.3 8 C7.3 10.3 9.7 12.7 12 13.7 L14 12 L17.5 15 L15.5 17.5 C9 17 3 11 2.5 4.5 Z" fill="var(--gold)"/>
        <path d="M12 3.5 A5 5 0 0 1 16.5 8" stroke="var(--gold)" stroke-width="1.6" fill="none" stroke-linecap="round"/>
      </svg>
      <span>555-214-6038</span>
    </li>
    <li class="contact__item">
      <svg class="contact__icon" viewBox="0 0 20 20" aria-hidden="true">
        <circle cx="10" cy="10" r="8" fill="var(--gold)"/>
        <path d="M2.5 10 H17.5 M10 2 C6.5 6 6.5 14 10 18 M10 2 C13.5 6 13.5 14 10 18" stroke="#fff" stroke-width="1.3" fill="none"/>
      </svg>
      <span>www.BrightLensStudio.example</span>
    </li>
    <li class="contact__item">
      <svg class="contact__icon" viewBox="0 0 20 20" aria-hidden="true">
        <path d="M10 1.5 C6.4 1.5 4 4.2 4 7.4 C4 11.5 10 18.5 10 18.5 C10 18.5 16 11.5 16 7.4 C16 4.2 13.6 1.5 10 1.5 Z" fill="var(--gold)"/>
        <circle cx="10" cy="7.4" r="2.3" fill="#fff"/>
      </svg>
      <span>418 Harlan P. Moody, Fairhaven Springs, NV 70000</span>
    </li>
  </ul>
</section>

<section class="card card--back">
  <div class="brand">
    <span class="brand__dot"></span>
    <span class="brand__name">Bright Lens Studio</span>
  </div>
</section>

</body>
</html>
```